Specialty Coffee Company- Need Gift Card Design

We need a new design with our new logo for our gift card. Use attached logo. Can use white logo on dark background or our dark brown logo color on lighter background. Possibly have some sort of modern coffee related background. Only need front of card designed.

```html
<!DOCTYPE html>
<html lang="en">
<head>
<meta charset="utf-8">
<title>Corvallo Gift Card – Front Design Proofs</title>
<link rel="stylesheet" href="https://fonts.googleapis.com/css2?family=Nunito:wght@800&family=PT+Sans&display=swap">
<style>
  :root {
    --paper: #ffffff;
    --ink: #111111;
    --roast-dark: #5e3817;
    --roast-glow: #7b4c29;
    --latte: #dfc5b6;
    --espresso: #4a2813;
    --cream: #ffffff;
    --ochre: #8f6a33;
    --ochre-deep: #6e4a22;
    --orange-accent: #c9782e;
    --blush: #f3e6da;
    --rose: #d9a79a;
    --berry: #a8383c;
    --guide-bleed: #e8403a;
    --guide-cut: #2aa5dc;
    --guide-safe: #e8403a;
  }
  html, body {
    margin: 0;
    padding: 0;
    width: 1200px;
    height: 1132px;
    overflow: hidden;
    background: var(--paper);
  }
  .sheet { display: block; width: 1200px; height: 1132px; }
  .guide-label {
    font-family: "PT Sans", "Myriad Pro", Arial, sans-serif;
    font-size: 37px;
    fill: var(--ink);
  }
  .guide-leader { stroke: var(--ink); stroke-width: 1.4; }
  .guide-bleed { fill: none; stroke: var(--guide-bleed); stroke-width: 2.6; }
  .guide-cut { fill: none; stroke: var(--guide-cut); stroke-width: 2.6; }
  .guide-safe { fill: none; stroke: var(--guide-safe); stroke-width: 2.6; }
  .brand-name {
    font-family: "Nunito", "Arial Rounded MT Bold", sans-serif;
    font-weight: 800;
    font-size: 96px;
    letter-spacing: -1px;
  }
  .brand-tagline {
    font-family: "Nunito", "Arial Rounded MT Bold", sans-serif;
    font-weight: 800;
    font-size: 37px;
    text-anchor: end;
    letter-spacing: 0.5px;
  }
  .card-dark .brand-name,
  .card-dark .brand-tagline,
  .card-dark .brand-dot { fill: var(--cream); }
  .card-light .brand-name,
  .card-light .brand-tagline,
  .card-light .brand-dot { fill: var(--espresso); }
  .card-dark .card-ground { fill: url(#roastGlow); }
  .card-light .card-ground { fill: var(--latte); }
  .card-dark .flourish { fill: url(#flourishDark); }
  .card-light .flourish { fill: url(#flourishLight); }
</style>
</head>
<body>
<svg class="sheet" viewBox="0 0 1200 1132" xmlns="http://www.w3.org/2000/svg">
  <defs>
    <radialGradient id="roastGlow" cx="760" cy="260" r="420" gradientUnits="userSpaceOnUse">
      <stop offset="0" stop-color="var(--roast-glow)"/>
      <stop offset="0.55" stop-color="var(--roast-dark)"/>
      <stop offset="1" stop-color="var(--roast-dark)"/>
    </radialGradient>
    <linearGradient id="flourishDark" x1="0" y1="0" x2="1" y2="1">
      <stop offset="0" stop-color="var(--ochre)"/>
      <stop offset="0.5" stop-color="var(--ochre-deep)"/>
      <stop offset="1" stop-color="var(--ochre)"/>
    </linearGradient>
    <linearGradient id="flourishLight" x1="0" y1="0" x2="1" y2="1">
      <stop offset="0" stop-color="var(--blush)"/>
      <stop offset="0.55" stop-color="var(--rose)"/>
      <stop offset="1" stop-color="var(--blush)"/>
    </linearGradient>
  </defs>

  <!-- Dark card proof -->
  <g class="card card-dark">
    <rect class="card-ground" x="290" y="2" width="908" height="545" rx="24"/>
    <path class="flourish" role="img" aria-label="Swirling floral flourish with grunge texture in browns and orange"
          d="M352,63 H530 Q548,140 486,200 Q440,250 382,280 H352 Z"/>
    <path class="flourish" role="img" aria-label="Swirling floral flourish with grunge texture in browns and orange"
          d="M1137,290 V485 H955 Q958,420 1020,392 Q1062,320 1137,290 Z"/>
    <circle class="brand-dot" cx="565" cy="237" r="34"/>
    <text class="brand-name" x="612" y="270">Corvallo</text>
    <text class="brand-tagline" x="918" y="436">fresh roasted</text>
    <rect class="guide-bleed" x="290" y="2" width="908" height="545" rx="24"/>
    <rect class="guide-cut" x="320" y="31" width="848" height="485" rx="24"/>
    <rect class="guide-safe" x="350" y="61" width="788" height="425"/>
  </g>

  <g class="guide-legend">
    <text class="guide-label" x="14" y="77">Bleed</text>
    <line class="guide-leader" x1="146" y1="60" x2="292" y2="60"/>
    <text class="guide-label" x="124" y="142">Cut</text>
    <line class="guide-leader" x1="200" y1="127" x2="321" y2="127"/>
    <text class="guide-label" x="45" y="204">Safe</text>
    <line class="guide-leader" x1="118" y1="193" x2="353" y2="193"/>
  </g>

  <!-- Light card proof -->
  <g class="card card-light">
    <rect class="card-ground" x="289" y="586" width="909" height="544" rx="24"/>
    <path class="flourish" role="img" aria-label="Swirling floral flourish in burgundy, rose and cream"
          d="M912,648 H1136 V885 Q1060,900 1005,865 Q992,760 912,705 Z"/>
    <path class="flourish" role="img" aria-label="Swirling floral flourish in burgundy, rose and cream"
          d="M352,900 Q400,842 470,852 Q560,900 585,1000 L585,1068 H352 Z"/>
    <circle class="brand-dot" cx="556" cy="818" r="34"/>
    <text class="brand-name" x="603" y="851">Corvallo</text>
    <text class="brand-tagline" x="911" y="1016">fresh roasted</text>
    <rect class="guide-bleed" x="289" y="586" width="909" height="544" rx="24"/>
    <rect class="guide-cut" x="320" y="616" width="848" height="484" rx="24"/>
    <rect class="guide-safe" x="349" y="646" width="788" height="424"/>
  </g>

  <g class="guide-legend">
    <text class="guide-label" x="0" y="662">Bleed</text>
    <line class="guide-leader" x1="145" y1="644" x2="290" y2="644"/>
    <text class="guide-label" x="111" y="727">Cut</text>
    <line class="guide-leader" x1="199" y1="712" x2="320" y2="712"/>
    <text class="guide-label" x="32" y="789">Safe</text>
    <line class="guide-leader" x1="118" y1="777" x2="353" y2="777"/>
  </g>
</svg>
</body>
</html>
```